Simple proffessional BC

I have a logo which I will attach below.
I would like the logo on the front of the card with these details in point form below:
Pre and Post Natal Yoga: Pregnancy Workshops: Hypnobirthing Courses
On the back of the card my details:
Marla Penrick
Facebook page- calmcradlestudiolakebay
Mobile- 0482 315 746

I like the idea of the card being simple, possibly just the above on a plain coloured (eggshell?) card, a card that is textured.
I am open to suggestion if it appeals!
Thank you and good luck!

Target Market(s)

Pregnant women, 20's-40's

Requirements
Must have
• Simple, compliment logo.
Make logo the feature.
Should not have

```html
<!DOCTYPE html>
<html lang="en">
<head>
<meta charset="utf-8">
<title>Calm Cradle – Business Card</title>
<link rel="stylesheet" href="https://fonts.googleapis.com/css2?family=Mulish:wght@400;700;800&display=swap">
<style>
  :root {
    --bg-light: #f2bd5a;
    --bg-deep: #f0960f;
    --wine-bright: #d4172a;
    --wine: #98071a;
    --wine-deep: #6e040f;
    --maroon: #5e0008;
    --amber: #ee9a10;
    --paper: #ffffff;
    --label: #4e1608;
    --ink: #7a0a14;
  }
  * { margin: 0; padding: 0; box-sizing: border-box; }
  html, body { width: 1200px; height: 1000px; overflow: hidden; }
  body {
    position: relative;
    background: radial-gradient(ellipse 60% 60% at 50% 50%, var(--bg-light) 0%, var(--bg-deep) 100%);
    font-family: "Mulish", sans-serif;
  }
  .side-label {
    position: absolute;
    font-size: 30px;
    color: var(--label);
    font-weight: 400;
  }
  .side-label--back { left: 176px; top: 386px; }
  .side-label--front { left: 334px; top: 764px; }

  .card {
    position: absolute;
    width: 646px;
    height: 378px;
    transform-origin: 0 0;
    transform: rotate(-22.8deg);
    overflow: hidden;
  }
  .card--back {
    left: 150px; top: 263px;
    background: radial-gradient(ellipse 55% 70% at 50% 32%, var(--wine-bright) 0%, var(--wine) 55%, var(--wine-deep) 100%);
  }
  .card--front {
    left: 307px; top: 636px;
    background: var(--paper);
  }
  .card__layer { position: absolute; left: 0; top: 0; }

  .mark-circle {
    position: absolute;
    border-radius: 50%;
    background: var(--amber);
  }
  .card--back .mark-circle {
    left: 284px; top: 94px; width: 76px; height: 76px;
    box-shadow: 0 0 0 2px var(--wine-bright), 0 0 0 3px var(--amber);
  }
  .card--front .mark-circle {
    left: 78px; top: 59px; width: 46px; height: 46px;
  }

  .holder-name {
    position: absolute;
    left: 40px; top: 281px;
    font-size: 22px;
    font-weight: 800;
    color: var(--maroon);
    line-height: 26px;
  }
  .contact {
    position: absolute;
    left: 322px; top: 262px;
    font-size: 12.5px;
    font-weight: 700;
    color: var(--maroon);
    line-height: 22px;
    letter-spacing: 0.3px;
  }

  .brand-name {
    position: absolute;
    left: 134px; top: 64px;
    font-size: 28px;
    font-weight: 400;
    color: var(--ink);
    line-height: 34px;
    letter-spacing: 0.5px;
  }
  .services {
    position: absolute;
    left: 322px; top: 254px;
    list-style: none;
    font-size: 19px;
    font-weight: 400;
    color: var(--ink);
    line-height: 29px;
  }
  .services li { display: flex; align-items: center; }
  .services li::before {
    content: "";
    width: 8px; height: 8px;
    border-radius: 50%;
    margin-right: 6px;
    background: radial-gradient(circle at 35% 35%, var(--amber), #a3400a);
  }
</style>
</head>
<body>
  <span class="side-label side-label--back">B</span>
  <span class="side-label side-label--front">F</span>

  <section class="card card--back" aria-label="Card back">
    <svg class="card__layer" width="646" height="378" viewBox="0 0 646 378" aria-hidden="true">
      <polygon class="name-band" points="0,277 328,277 342,252 646,252 646,317 0,317" fill="var(--amber)"/>
    </svg>
    <div class="mark-circle" aria-hidden="true"></div>
    <p class="holder-name">Marla Penrick</p>
    <p class="contact">facebook Page : calmcradlestudiolakebay<br>Mobile : 0482 315 746</p>
  </section>

  <section class="card card--front" aria-label="Card front">
    <svg class="card__layer" width="646" height="378" viewBox="0 0 646 378" aria-hidden="true">
      <g class="stripe-block stripe-block--left">
        <rect x="0" y="54" width="72" height="20" fill="var(--maroon)"/>
        <rect x="0" y="74" width="72" height="6" fill="var(--amber)"/>
        <rect x="0" y="80" width="72" height="22" fill="var(--maroon)"/>
      </g>
      <g class="stripe-block stripe-block--right">
        <rect x="334" y="52" width="312" height="22" fill="var(--maroon)"/>
        <rect x="334" y="74" width="312" height="6" fill="var(--amber)"/>
        <rect x="334" y="80" width="312" height="24" fill="var(--maroon)"/>
      </g>
    </svg>
    <div class="mark-circle" aria-hidden="true"></div>
    <p class="brand-name">Calm Cradle</p>
    <ul class="services">
      <li>Pre and Post Natal Yoga</li>
      <li>Pregnancy Workshops</li>
      <li>Hypnobirthing Courses</li>
    </ul>
  </section>
</body>
</html>
```